**URGENT // ENVIRONMENTAL // QUICK TURN AROUND**

We are looking for an A-Grade designer to work with longterm, starting with the successful design for our website & logo; Pelham Grove.

Pelham Grove is a business that focusses on grouping environmentally conscious people together and helping them get "bulk buy" discounts by purchasing large volumes together; solar, energy efficency, wind turbines, and the like.

The Logo and website must have a green feel, as we are here to protect the environment, whilst also helping our customers save money.

The website must also have a blog feature, allowing us to post and keep people up to date with the latest in the industry.

Target Market(s)

FAMILIES WITHIN REGIONAL AUSTRALIA WANTING TO EITHER SAVE MONEY ON ELECTRICITY BILLS, OR REDUCE CARBON EMISSIONS.

Industry/Entity Type

Solar Energy

Logo Text

PELHAM GROVE

Number of Pages Required

5+ page

Font styles to use
Serif
Sans Serif

Colors

Designer to choose colors to be used in the design.

Requirements
Must have
• 1.HOME PAGE
• 2.OUR SERVICES PAGE
• - RENEWABLE ENERGY
• - LIGHTING SYSTEMS
• - ENERGY ASSESSMENT
• - R.G.L.C SCHEME
• - ENERGY COMPARISON
• 4. BOOK AN APPOINTMENT
• 5. IN THE NEWS
• 6. SUBSCRIBE TO NEWSLETTER
• 7. CONTACT US
• MUST LOOK VERY PROFESSIONAL, WITH LOTS OF INFORMATION, IT CANNOT BE BARE AND SIMPLE.
• Can use www.marlowfieldtrading.com.au which is our other brand for copy and ideas - HOWEVER, THIS IS THE REASON WE ARE RE-BRANDING, AS THIS BRAND HAS COME UNDER FAR TOO MUCH CRITICISM FOR LACK OF INFORMATION AND LOOKING TO SIMPLE.
Nice to have
• BLOG FEATURE
Should not have
• ANYTHING THAT APPEARS NON-ENVIRONMENTALS

```html
<!DOCTYPE html>
<html lang="en">
<head>
<meta charset="utf-8">
<title>Pelham Grove — Energy Saving Services</title>
<link href="https://fonts.googleapis.com/css2?family=Montserrat:wght@400;600;700;800&family=Open+Sans:wght@400;600;700&display=swap" rel="stylesheet">
<style>
:root{
  --green:#6ac21a;
  --green-dark:#58a812;
  --ink:#222222;
  --text:#666666;
  --muted:#999999;
  --dark:#1b1b1b;
  --darker:#141414;
  --light:#f2f2f2;
  --placeholder:#7b7b7b;
  --white:#ffffff;
  --grey-band:#8c8c8c;
}
*{box-sizing:border-box;margin:0;padding:0}
html,body{width:1200px;height:3805px;overflow:hidden}
body{font-family:"Open Sans",Arial,sans-serif;color:var(--text);background:var(--white);font-size:13px;line-height:1.6}
h1,h2,h3,h4,.head{font-family:"Montserrat",Helvetica,sans-serif;color:var(--ink)}
.green{color:var(--green)}
section,header,footer{position:relative;width:1200px;overflow:hidden}
.btn{display:inline-block;font-family:"Montserrat",sans-serif;font-size:10px;font-weight:700;letter-spacing:.5px;padding:9px 18px;border:1px solid #cfcfcf;color:var(--ink);background:var(--white);text-transform:uppercase}
.btn-green{background:var(--green);border-color:var(--green);color:var(--white)}
.btn-ghost{background:transparent;border-color:var(--white);color:var(--white)}

/* header */
.site-header{height:81px;border-bottom:4px solid var(--green)}
.topbar{position:absolute;right:0;top:0;width:600px;height:20px;background:var(--dark);color:#ccc;font-size:10px;display:flex;align-items:center;gap:40px;padding-left:50px}
.topbar .social{display:flex;gap:8px;margin-left:auto;margin-right:50px}
.dot{width:9px;height:9px;border-radius:50%;background:#bdbdbd;display:inline-block}
.brand{position:absolute;left:240px;top:12px;display:flex;align-items:center;gap:10px}
.brand-mark{width:52px;height:52px;border-radius:50%;background:var(--green)}
.brand-name{font-family:"Montserrat",sans-serif;font-weight:700;font-size:22px;color:var(--green);line-height:1}
.brand-tag{font-size:8px;color:var(--muted);letter-spacing:1px;margin-top:4px}
.nav{position:absolute;right:235px;top:40px;display:flex;align-items:center;gap:22px;font-family:"Montserrat",sans-serif;font-size:10px;font-weight:600;color:var(--ink)}
.nav .btn{padding:6px 12px;border-radius:12px;font-size:9px}

/* hero */
.hero{height:490px;background:linear-gradient(160deg,#c8d4de 0%,#8ea3b6 35%,#4a6788 60%,#b9b3a6 100%)}
.hero-copy{position:absolute;left:279px;top:165px;color:var(--white)}
.hero-copy h1{color:var(--white);font-size:62px;font-weight:800;letter-spacing:1px;line-height:1}
.hero-copy .strap{display:inline-block;background:var(--green);color:var(--white);font-family:"Montserrat",sans-serif;font-weight:700;font-size:15px;padding:4px 14px;margin-top:8px}
.hero-copy p{font-size:11px;margin:10px 0 14px;width:300px}

/* services */
.services{height:444px;text-align:center}
.services h2{font-size:46px;font-weight:800;color:var(--green);margin-top:50px;line-height:1.1}
.services .sub{font-family:"Montserrat",sans-serif;font-size:20px;color:var(--ink);font-weight:600}
.services .lead{font-size:11px;margin-top:14px}
.service-list{display:flex;justify-content:center;gap:38px;margin-top:48px}
.service{width:152px;height:152px;border-radius:50% 0 50% 50%;background:var(--green);color:var(--white);display:flex;flex-direction:column;align-items:center;justify-content:center;gap:16px;font-family:"Montserrat",sans-serif;font-weight:700;font-size:10px}

/* appointment */
.appointment{height:330px;display:flex}
.appointment .photo{width:601px;height:100%;background:linear-gradient(150deg,#6d9bd6 0%,#3e6db4 45%,#2a3f78 75%,#7b5d4a 100%)}
.appointment .copy{flex:1;background:var(--dark);color:#ddd;padding:50px 60px 0 52px}
.appointment h2{color:var(--white);font-size:22px;font-weight:800;line-height:1.2}
.appointment .intro{font-size:11px;margin:6px 0 38px}
.appointment p{font-size:10px;line-height:1.6;width:380px}
.appointment .actions{margin-top:48px;display:flex;gap:14px}

/* projects */
.projects{height:487px;padding:0 233px}
.projects-head{display:flex;justify-content:space-between;align-items:flex-start;padding-top:60px}
.projects h2{font-size:26px;font-weight:800}
.projects h2 .green{font-weight:600}
.projects .intro{font-size:11px}
.project-grid{display:flex;gap:18px;margin-top:38px}
.project{width:170px}
.project .thumb{height:120px;background:var(--placeholder)}
.project h4{font-size:10px;font-weight:700;margin-top:18px}
.project .cat{font-size:9px;color:var(--green)}
.project p{font-size:9px;color:var(--muted);margin:8px 0 14px;line-height:1.5}
.project .btn{padding:6px 14px;font-size:8px}

/* facts & ceo */
.facts-ceo{height:325px;display:flex}
.facts{width:601px;background:var(--light);padding:60px 60px 0 233px}
.facts h2,.ceo h2{font-size:24px;font-weight:800}
.rule{width:28px;height:3px;background:var(--green);margin:6px 0 14px}
.facts p{font-size:10px;color:var(--muted);line-height:1.6}
.facts .lead{font-size:11px;color:var(--text)}
.stats{display:flex;gap:48px;margin-top:22px}
.stat{text-align:center}
.stat b{display:block;font-family:"Montserrat",sans-serif;font-size:20px;color:var(--ink);margin-top:6px}
.stat span{font-size:8px;text-transform:uppercase;color:var(--muted)}
.ceo{flex:1;background:var(--green);color:var(--white);padding:54px 60px 0 52px}
.ceo h2{color:var(--white)}
.ceo .row{display:flex;gap:18px}
.quote-badge{width:40px;height:40px;border-radius:50%;border:2px solid var(--white);flex:none;display:flex;align-items:center;justify-content:center;font-family:Georgia,serif;font-size:26px;line-height:1}
.ceo p{font-size:10px;line-height:1.6;margin-top:14px;width:300px}
.ceo .person{display:flex;gap:10px;margin-top:20px;align-items:center}
.avatar{width:44px;height:44px;background:#e8e8e8}
.ceo .person b{display:block;font-size:11px}
.ceo .person span{font-size:9px}
.signature{width:150px;height:36px;margin-top:16px;margin-left:62px;background:linear-gradient(90deg,rgba(255,255,255,.5),rgba(255,255,255,.15));border-radius:18px}

/* blog */
.blog{height:533px;text-align:center}
.blog h2{font-size:26px;font-weight:600;margin-top:64px}
.blog h2 b{font-weight:800}
.blog .intro{font-size:11px;margin-top:4px}
.post-grid{display:flex;gap:35px;justify-content:center;margin-top:38px;text-align:left}
.post{width:221px}
.post .thumb{position:relative;height:152px;background:var(--placeholder)}
.date{position:absolute;left:12px;top:-2px;width:40px;height:44px;border-radius:0 0 20px 20px;background:var(--green);color:var(--white);text-align:center;font-family:"Montserrat",sans-serif;font-weight:700;line-height:1;padding-top:6px}
.date b{display:block;font-size:16px}
.date span{font-size:8px}
.post h4{font-size:13px;font-weight:600;margin-top:18px}
.post .meta{display:flex;justify-content:space-between;font-size:8px;color:var(--muted);margin-top:4px}
.post p{font-size:9px;color:var(--muted);line-height:1.6;margin:10px 0 14px}
.post .more{font-family:"Montserrat",sans-serif;font-size:9px;font-weight:700;color:var(--ink)}

/* testimonials */
.testimonials{height:426px;background:var(--grey-band);text-align:center;color:var(--white)}
.testimonials h2{color:var(--white);font-size:26px;font-weight:800;margin-top:64px;letter-spacing:1px}
.testimonials .intro{font-size:11px}
.testi-grid{display:flex;gap:35px;justify-content:center;margin-top:58px}
.testi{position:relative;width:221px;height:120px;background:var(--white);color:var(--text);padding:16px 20px 0 34px;text-align:left}
.testi .avatar{position:absolute;left:28px;top:-18px;width:56px;height:56px;border-radius:50%;background:#f0f0f0}
.testi .who{margin-left:66px;font-family:"Montserrat",sans-serif;font-size:10px;font-weight:700;color:var(--ink)}
.testi .who span{display:block;font-size:8px;color:var(--green);font-weight:600}
.testi p{font-size:9px;margin-top:16px;line-height:1.5}
.arrows{display:flex;gap:4px;justify-content:center;margin-top:30px}
.arrows span{width:24px;height:22px;background:var(--green);display:flex;align-items:center;justify-content:center}
.arrows span:first-child{background:#6e6e6e}

/* tree banner */
.tree-banner{height:271px;background:linear-gradient(180deg,#1e4f8a 0%,#3f7cc0 45%,#9cc3e8 75%,#6b8fb8 100%);text-align:center;color:var(--white)}
.tree-banner h2{color:var(--white);font-size:26px;font-weight:700;margin-top:82px}
.tree-banner p{font-size:14px}
.tree-banner .btn{margin-top:20px;padding:10px 22px}

/* newsletter */
.newsletter{height:114px;background:var(--green);color:var(--white);padding:30px 233px 0;display:flex;justify-content:space-between}
.newsletter h3{color:var(--white);font-size:18px;font-weight:600}
.newsletter p{font-size:11px}
.newsletter .btn{margin-top:10px;height:32px}

/* footer */
.site-footer{height:304px;background:var(--darker);color:#aaa;padding:40px 233px 0;display:flex;gap:40px}
.f-about{width:200px}
.f-about .brand{position:static}
.f-about .brand-mark{width:48px;height:48px}
.f-about p{font-size:10px;margin:16px 0 10px}
.f-contact li{list-style:none;font-size:9px;display:flex;gap:8px;align-items:center;margin-bottom:8px}
.f-contact i{width:8px;height:8px;background:var(--green);display:inline-block}
.f-social{display:flex;gap:6px;margin-top:10px}
.f-social span{width:14px;height:14px;border-radius:50%;border:1px solid #888}
.f-social span:first-child{background:var(--green);border-color:var(--green)}
.f-col h4{color:var(--white);font-size:11px;font-weight:700;margin:14px 0 18px}
.f-col li{list-style:none;font-size:9px;margin-bottom:7px}
.f-projects{width:110px}
.f-news{width:210px}
.news-item{display:flex;gap:10px;margin-bottom:16px;font-size:9px;line-height:1.4}
.news-item .thumb{width:44px;height:40px;background:#666;flex:none}
.news-item span{display:block;color:#777;font-size:8px}
.f-links{width:110px;margin-left:auto}
.copyright{position:absolute;left:0;right:0;bottom:14px;text-align:center;font-size:8px;color:#777}
</style>
</head>
<body>

<header class="site-header">
  <div class="topbar">
    <span>hello@pelhamgrove.com.au</span>
    <span>(700) 555-0142</span>
    <span class="social"><i class="dot"></i><i class="dot"></i><i class="dot"></i><i class="dot"></i></span>
  </div>
  <div class="brand">
    <span class="brand-mark"></span>
    <div>
      <div class="brand-name">PELHAM GROVE</div>
      <div class="brand-tag">BEST ENERGY SAVING SERVICES</div>
    </div>
  </div>
  <nav class="nav">
    <span>HOME</span><span>ABOUT</span><span>SERVICES</span><span>BLOG</span><span>CONTACT US</span>
    <span class="btn btn-green">BOOK APPOINTMENT</span>
  </nav>
</header>

<section class="hero" role="img" aria-label="Photo of two engineers in hard hats and safety vests inspecting rooftop solar panels">
  <div class="hero-copy">
    <h1>ECO SOLAR</h1>
    <div class="strap">BEST ENERGY SAVING SERVICES</div>
    <p>Lower bills and cleaner power for every family in the region.</p>
    <span class="btn btn-ghost">LEARN MORE</span>
  </div>
</section>

<section class="services">
  <h2>OUR SERVICES</h2>
  <div class="sub">OUR SERVICES</div>
  <p class="lead">Lorem ipsum dolor sit amet, pro in harum epicid persecuti, eu mea minim platonem, mea ceteris intellegam eu. Mel fem</p>
  <div class="service-list">
    <div class="service">
      <svg width="40" height="40" viewBox="0 0 40 40" fill="none" stroke="#fff" stroke-width="2"><circle cx="20" cy="20" r="18"/><path d="M20 10a6 6 0 0 0-4 10.5V25h8v-4.5A6 6 0 0 0 20 10zM17 28h6"/></svg>
      LIGHTING SYSTEMS
    </div>
    <div class="service">
      <svg width="40" height="40" viewBox="0 0 40 40" fill="none" stroke="#fff" stroke-width="2"><path d="M20 6l7 12H13zM8 32l6-11 6 11zM26 32l6-11 4 11z"/></svg>
      RENEWABLE ENERGY
    </div>
    <div class="service">
      <svg width="40" height="40" viewBox="0 0 40 40" fill="none" stroke="#fff" stroke-width="2"><path d="M20 6c6 9 10 14 10 19a10 10 0 0 1-20 0c0-5 4-10 10-19z"/></svg>
      R.G.L.C SCHEME
    </div>
    <div class="service">
      <svg width="40" height="40" viewBox="0 0 40 40" fill="none" stroke="#fff" stroke-width="2"><circle cx="20" cy="22" r="7"/><path d="M20 6v5M8 12l3 3M32 12l-3 3M4 22h5M31 22h5"/></svg>
      ENERGY ASSESSMENT
    </div>
  </div>
</section>

<section class="appointment">
  <div class="photo" role="img" aria-label="Photo of a technician in a hard hat installing solar panels on a roof under blue sky"></div>
  <div class="copy">
    <h2>BOOK <span class="green">AN APPOINTMENT</span><br>NOW</h2>
    <p class="intro">Lorem ipsum dolor <b class="green">some link</b> sit amet, cum at inani interesset</p>
    <p>Lorem ipsum dolor sit amet, eu qui modo expetendis reformidans ex sit vel apeirian sententiae nec ut ea stet in utroque habemus. Duo cetero possit probatus no qu dicto sit ad alii vix simple dummy.</p>
    <div class="actions"><span class="btn">BOOK NOW</span><span class="btn btn-green">VIEW DETAILS</span></div>
  </div>
</section>

<section class="projects">
  <div class="projects-head">
    <div>
      <h2>RECENT <span class="green">PROJECT</span></h2>
      <p class="intro">Lorem ipsum dolor sit amet, cum at inani interesset, nisl fugit munere ad mel ex an omnium dolor amet</p>
    </div>
    <span class="btn" style="margin-top:6px">SEE ALL PROJECT</span>
  </div>
  <div class="project-grid">
    <div class="project"><div class="thumb" role="img" aria-label="Project photo"></div><h4>PROJECT NAME</h4><div class="cat">Environmental, Go Green Company</div><p>Lorem ipsum dolor sit amet id sit amet quidam suspendisse nec porta vitae aliquam nunc.</p><span class="btn">LEARN MORE</span></div>
    <div class="project"><div class="thumb" role="img" aria-label="Project photo"></div><h4>PROJECT NAME</h4><div class="cat">Environmental, Go Green Company</div><p>Lorem ipsum dolor sit amet id sit amet quidam suspendisse nec porta vitae aliquam nunc.</p><span class="btn">LEARN MORE</span></div>
    <div class="project"><div class="thumb" role="img" aria-label="Project photo"></div><h4>PROJECT NAME</h4><div class="cat">Environmental, Go Green Company</div><p>Lorem ipsum dolor sit amet id sit amet quidam suspendisse nec porta vitae aliquam nunc.</p><span class="btn">LEARN MORE</span></div>
    <div class="project"><div class="thumb" role="img" aria-label="Project photo"></div><h4>PROJECT NAME</h4><div class="cat">Environmental, Go Green Company</div><p>Lorem ipsum dolor sit amet id sit amet quidam suspendisse nec porta vitae aliquam nunc.</p><span class="btn">LEARN MORE</span></div>
  </div>
</section>

<section class="facts-ceo">
  <div class="facts">
    <h2>SOME <span class="green">FACTS</span></h2>
    <div class="rule"></div>
    <p class="lead">Lorem ipsum dolor some link sit amet, cum at inani interesset</p>
    <p>We're extremely proud of what we've achieved together with like-minded families, local partners and schools since the day this firm was founded in 2007, and here are some facts from our achievement.</p>
    <div class="stats">
      <div class="stat">
        <svg width="22" height="26" viewBox="0 0 22 26" fill="none" stroke="#6ac21a" stroke-width="2"><path d="M2 2h12l6 6v16H2z"/><path d="M6 13h10M6 18h10"/></svg>
        <b>412</b><span>Projects</span>
      </div>
      <div class="stat">
        <svg width="30" height="26" viewBox="0 0 30 26" fill="none" stroke="#6ac21a" stroke-width="2"><circle cx="11" cy="14" r="9"/><circle cx="20" cy="10" r="8"/></svg>
        <b>305</b><span>People loved us</span>
      </div>
    </div>
  </div>
  <div class="ceo">
    <div class="row">
      <div class="quote-badge">“</div>
      <div>
        <h2>WORD FROM <span style="font-weight:600">CEO</span></h2>
        <p>We're extremely proud of what we've achieved together with like-minded families, local partners and schools since the day this firm was founded in 2007, and here are some facts from our achievement.</p>
        <div class="person">
          <div class="avatar" role="img" aria-label="Portrait of the CEO"></div>
          <div><b>Rowan Tesh</b><span>CEO of Pelham Grove</span></div>
        </div>
      </div>
    </div>
    <div class="signature" role="img" aria-label="Handwritten signature of the CEO"></div>
  </div>
</section>

<section class="blog">
  <h2>LATEST <b class="green">ON OUR BLOG</b></h2>
  <p class="intro">Lorem ipsum dolor sit amet, cum at inani interesset nisl munere ad mel ex an omnium dolor amet quo modo cum text</p>
  <div class="post-grid">
    <article class="post"><div class="thumb" role="img" aria-label="Blog photo of melting ice"><div class="date"><b>28</b><span>OCT</span></div></div><h4>Melting ice</h4><div class="meta"><span>Posted by admin, Energy</span><span>♡ 6 &nbsp; ▢ 33</span></div><p>Lorem ipsum dolor sit amet, consectetur adipi elit sed do eiusmod tempor incididunt ut labore dolore et dolore magna aliqua ornare...</p><span class="more">READ MORE</span></article>
    <article class="post"><div class="thumb" role="img" aria-label="Blog photo of a cleared forest"><div class="date"><b>28</b><span>OCT</span></div></div><h4>Deforestation is the threat</h4><div class="meta"><span>Posted by admin, Energy</span><span>♡ 6 &nbsp; ▢ 33</span></div><p>Lorem ipsum dolor sit amet, consectetur adipi elit sed do eiusmod tempor incididunt ut labore dolore et dolore magna aliqua ornare...</p><span class="more">READ MORE</span></article>
    <article class="post"><div class="thumb" role="img" aria-label="Blog photo of wildlife"><div class="date"><b>28</b><span>OCT</span></div></div><h4>Save the animals</h4><div class="meta"><span>Posted by admin, Energy</span><span>♡ 6 &nbsp; ▢ 33</span></div><p>Lorem ipsum dolor sit amet, consectetur adipi elit sed do eiusmod tempor incididunt ut labore dolore et dolore magna aliqua ornare...</p><span class="more">READ MORE</span></article>
  </div>
</section>

<section class="testimonials">
  <h2>TESTI<span class="green">MONIALS</span></h2>
  <p class="intro">Lorem ipsum dolor sit amet, pro in harum epicid persecuti, eu mea minim platonem, mea ceteris intellegam eu</p>
  <div class="testi-grid">
    <div class="testi"><div class="avatar" role="img" aria-label="Customer portrait"></div><div class="who">LEO FARRANT<span>Home Owner</span></div><p>"But I must explain to you how all this mistaken idea of lower power bills was born so quickly"</p></div>
    <div class="testi"><div class="avatar" role="img" aria-label="Customer portrait"></div><div class="who">LEO FARRANT<span>Home Owner</span></div><p>"But I must explain to you how all this mistaken idea of lower power bills was born so quickly"</p></div>
    <div class="testi"><div class="avatar" role="img" aria-label="Customer portrait"></div><div class="who">LEO FARRANT<span>Home Owner</span></div><p>"But I must explain to you how all this mistaken idea of lower power bills was born so quickly"</p></div>
  </div>
  <div class="arrows">
    <span><svg width="8" height="10" viewBox="0 0 8 10"><path d="M6 1L2 5l4 4" stroke="#fff" stroke-width="2" fill="none"/></svg></span>
    <span><svg width="8" height="10" viewBox="0 0 8 10"><path d="M2 1l4 4-4 4" stroke="#fff" stroke-width="2" fill="none"/></svg></span>
  </div>
</section>

<section class="tree-banner" role="img" aria-label="Photo of a blue sky with soft white clouds">
  <h2>BOOK APPOINTMENT NOW AND <span class="green">HELP PLANT A TREE</span></h2>
  <p>Some lorem ipsum subtitle will be here ipsum dolor</p>
  <span class="btn btn-green">BOOK NOW</span>
</section>

<section class="newsletter">
  <div>
    <h3>Subscriber for Newsletter</h3>
    <p>There are many variations of passages of Lorem Ipsum available but the majority have</p>
  </div>
  <span class="btn btn-ghost">SUBSCRIBE NOW</span>
</section>

<footer class="site-footer">
  <div class="f-about">
    <div class="brand">
      <span class="brand-mark"></span>
      <div>
        <div class="brand-name" style="font-size:18px">PELHAM GROVE</div>
        <div class="brand-tag">BEST ENERGY SAVING SERVICES</div>
      </div>
    </div>
    <p>Lorem ipsum dolor sit amet, eu vix</p>
    <ul class="f-contact">
      <li><i></i>14 Wattle Rd, Dubbo NSW 2830</li>
      <li><i></i>(02) 5550 1187</li>
      <li><i></i>info@pelhamgrove.com.au</li>
    </ul>
    <div class="f-social"><span></span><span></span><span></span><span></span><span></span></div>
  </div>
  <div class="f-col f-projects">
    <h4>OUR PROJECT</h4>
    <ul><li>Water Survey</li><li>Education for all</li><li>Treatment</li><li>Food Serving</li><li>Cloth</li><li>Solar Project</li></ul>
  </div>
  <div class="f-col f-news">
    <h4>LATEST NEWS</h4>
    <div class="news-item"><div class="thumb" role="img" aria-label="News thumbnail"></div><div>If you need a crown or lorem an implant you will pay it<span>July 2, 2016</span></div></div>
    <div class="news-item"><div class="thumb" role="img" aria-label="News thumbnail"></div><div>If you need a crown or lorem an implant you will pay it<span>July 2, 2016</span></div></div>
  </div>
  <div class="f-col f-links">
    <h4>QUICK LINKS</h4>
    <ul><li>Water Survey</li><li>Education for all</li><li>Treatment</li><li>Food Serving</li><li>Cloth</li><li>Solar Project</li></ul>
  </div>
  <div class="copyright">All Rights Reserved to Pelham Grove Website</div>
</footer>

</body>
</html>
```